Professional Engineering Web Design

Project Brief: Website Redesign for Mechanical Design Consultancy
Project Overview
I want to update and improve my current website to create a more professional, modern, and high-credibility online presence for my mechanical design consultancy.

Current site: https://valtrobuild.design/

The new website must communicate expertise, precision, and trust—matching the standard of top engineering and product design agencies.

Reference Websites (Style + Structure Inspiration)
These represent the quality, cleanliness, and professionalism I want to achieve:

https://plinthformworks.com/
https://www.zorvanta.com/
https://quellory-uk.com/
Brand Look
Professional, modern, engineering-focused aesthetic
Clean layouts and strong typography
High-quality imagery conveying precision, innovation, and mechanical expertise
Colour scheme and styling must follow my existing logo (attached in project)
Platform Requirements
The website must be built on WordPress
Should use a clean, flexible theme or modern page builder (Elementor, Gutenberg, Bricks, or similar)
Avoid overly complex custom coding so I can easily edit content later
Final deliverable must allow me to manage and update content without developer assistance
Functionality
Fast-loading, lightweight, and smooth user experience
Clean animations and transitions similar to the reference sites
Fully mobile responsive
Clear navigation and strong visual hierarchy
Contact forms optimised for lead generation
Optional: subtle scroll effects, case study sliders, icon animations, etc.
SEO Aspirations
Developer should recommend and implement a modern SEO strategy
Proper on-page SEO setup (titles, meta, schema, alt tags, heading structure)
Optimised site architecture for ranking and crawling
Aim: Generate leads through improved visibility and keyword targeting
Optional but useful: Brightline Systems Analytics, Brightline Systems Search Console setup
User Journeys
(Recommended structure)

The site should be crafted around clear, intuitive journeys for each type of visitor:

Potential new clients
Quickly understand what services I offer
View examples of past work / case studies
See credibility indicators (process, expertise, industries served)
Easily contact me or request a project discussion
Returning clients
Access updated portfolio items
Find contact details or book follow-up work easily
General visitors discovering through SEO
Be guided to Valtro Build Design service areas
Understand my value proposition quickly
Be invited to learn more or make contact
The developer should design the structure to support these journeys smoothly.

Maintenance Expectations
Website will be maintained by me, so it should be easy to update using relatively basic WordPress skills
Use modular templates and simple backend structure
Avoid unnecessary plugins
Provide brief handover documentation if required
Hosting Preferences
Site is currently hosted via a family member
Open to discussing moving to a paid, reliable hosting provider if preferable for performance and maintainability
Developer may advise on the best hosting setup for WordPress
Content
Most content can be taken from the existing website
Developer is welcome to suggest improvements to structure, layout, and imagery
Must remain easy for me to edit or add new content later (e.g., new projects)
Deliverables
Fully built WordPress website
Clean, professional, modern design inspired by the reference sites
Mobile-responsive across all devices
SEO-ready structure and optimisations
Transfer of website and admin rights
Any design assets, templates, or documentation used

```html
<!DOCTYPE html>
<html lang="en">
<head>
<meta charset="utf-8">
<title>Valtro Build Design – Mechanical CAD Design</title>
<link href="https://fonts.googleapis.com/css2?family=Montserrat:wght@500;600;700&family=Inter:wght@400;500;600&display=swap" rel="stylesheet">
<style>
:root{
  --blue:#2f62f0;
  --navy:#172a5e;
  --ink:#2b2b2b;
  --body:#555a66;
  --muted:#8a8f99;
  --grey-band:#f1f2f4;
  --footer:#232426;
  --white:#fff;
}
*{box-sizing:border-box;margin:0;padding:0}
html,body{width:1200px;height:4706px;overflow:hidden}
body{position:relative;font-family:"Inter",sans-serif;color:var(--ink);background:var(--white)}
.abs{position:absolute}
.bg-layer{position:absolute;left:0;top:0;width:1200px;height:4706px}
h1,h2,h3,.heading{font-family:"Montserrat",sans-serif}

/* top bar + header */
.topbar{left:0;top:0;width:1200px;height:34px;display:flex;justify-content:flex-end;align-items:center;gap:28px;padding-right:140px;font-size:12px;color:var(--body)}
.topbar .socials{display:flex;gap:10px}
.dot-sm{width:12px;height:12px;border-radius:50%;background:var(--blue);display:inline-block}
.topbar .item{display:flex;align-items:center;gap:8px}
.ic-circle{width:24px;height:24px;border-radius:50%;background:var(--blue);display:inline-flex;align-items:center;justify-content:center}
.header{left:0;top:34px;width:1200px;height:82px;display:flex;align-items:center;padding:0 140px}
.brand{display:flex;align-items:center;gap:12px}
.brand-mark{width:34px;height:34px;background:var(--blue)}
.brand-name{font-family:"Montserrat",sans-serif;font-weight:700;font-size:24px;color:var(--navy);line-height:1}
.nav{margin-left:auto;display:flex;align-items:center;gap:48px;font-family:"Montserrat",sans-serif;font-weight:600;font-size:12px}
.btn{display:inline-flex;align-items:center;justify-content:center;background:var(--blue);color:#fff;border-radius:22px;font-family:"Montserrat",sans-serif;font-weight:600;font-size:12px}
.nav .btn{height:42px;padding:0 26px}

/* hero */
.hero{left:0;top:116px;width:1200px;height:558px;background:linear-gradient(100deg,#1a2f6e 0%,#2146a8 45%,#3b6fe0 100%)}
.hero-title{left:140px;top:260px;color:#fff;font-weight:700;line-height:1.12}
.hero-title .l1{font-size:50px}
.hero-title .l2{font-size:62px}
.hero-sub{left:141px;top:418px;color:#fff;font-family:"Montserrat",sans-serif;font-weight:500;font-size:29px}
.hero-btn{left:141px;top:490px;width:129px;height:40px;font-size:11px}
.scroll-btn{left:565px;top:639px;width:70px;height:70px;border-radius:50%;background:#fff;box-shadow:0 8px 20px rgba(0,0,0,.12);display:flex;align-items:center;justify-content:center}

/* section heads */
.sec-head{left:0;width:1200px;text-align:center}
.sec-head h2{font-weight:500;font-size:24px;color:var(--ink)}
.divider{display:flex;align-items:center;justify-content:center;gap:8px;margin-top:14px}
.divider i{display:block;width:54px;height:1px;background:#b7bcc6}
.divider b{display:block;width:12px;height:12px;border-radius:50%;background:var(--blue)}
.sec-head p{margin-top:18px;font-size:15px;color:var(--body)}

/* about */
.photo{border-radius:4px}
.about-title{left:608px;top:830px;font-size:24px;font-weight:500}
.about-div{left:608px;top:875px;display:flex;align-items:center;gap:8px}
.about-div b{width:12px;height:12px;border-radius:50%;background:var(--blue)}
.about-div i{width:54px;height:1px;background:#b7bcc6}
.about-text{left:608px;top:908px;width:452px;font-size:14.5px;line-height:30px;color:var(--body)}
.ticks{left:608px;top:1104px;display:flex;gap:30px;font-size:15px;color:var(--ink)}
.ticks span{display:flex;align-items:center;gap:10px}
.dark-pill{left:608px;top:1170px;width:232px;height:44px;border-radius:22px;background:#3a3b3e;color:#fff;font-size:13px;display:flex;align-items:center;padding-left:28px}
.pill-ic{position:absolute;right:4px;top:4px;width:36px;height:36px;border-radius:50%;background:#fff;display:flex;align-items:center;justify-content:center}
.dots{background-image:radial-gradient(#cfd3da 1.5px,transparent 1.6px);background-size:10px 10px}

/* service cards */
.svc{width:282px;height:383px;background:#fff;border-radius:6px;box-shadow:0 4px 18px rgba(0,0,0,.06);text-align:center;padding-top:28px}
.svc .icon{width:64px;height:64px;border-radius:50%;background:var(--blue);margin:0 auto;display:flex;align-items:center;justify-content:center}
.svc .icon.dark{background:#3a3b3e}
.svc h3{font-size:16px;font-weight:600;margin-top:24px}
.svc p{font-size:13px;line-height:24px;color:var(--body);margin-top:12px;padding:0 14px}
.svc .pic{position:absolute;left:16px;top:205px;width:250px;height:162px;border-radius:4px}

/* work cards */
.work{width:282px;height:337px;background:#fff;border-radius:6px;box-shadow:0 4px 18px rgba(0,0,0,.07);overflow:hidden}
.work .pic{height:162px}
.work h3{font-family:"Inter",sans-serif;font-weight:500;font-size:15px;margin:30px 16px 0}
.work p{font-size:12px;line-height:22px;color:var(--body);margin:10px 16px 0}
.work .link{position:absolute;left:16px;bottom:22px;font-size:12px;font-weight:500;display:flex;align-items:center;gap:8px}
.cta-blue{left:497px;top:2592px;width:206px;height:46px;border-radius:23px;font-size:13px;font-family:"Inter",sans-serif;font-weight:500;justify-content:flex-start;padding-left:26px}
.cta-blue .pill-ic{top:5px;right:5px;width:36px;height:36px}

/* process */
.step{width:211px;height:230px;background:#fff;border-radius:4px;box-shadow:0 4px 18px rgba(0,0,0,.06);padding:22px 18px}
.step .hd{display:flex;align-items:center;gap:14px;font-size:15px;font-weight:500}
.step .ic{width:46px;height:46px;border-radius:50%;background:var(--blue);display:flex;align-items:center;justify-content:center}
.step p{font-size:12px;line-height:22px;color:var(--body);margin-top:22px}
.step .link{position:absolute;left:18px;bottom:24px;font-size:12px;font-weight:500;display:flex;gap:8px;align-items:center}
.step .num{position:absolute;right:14px;bottom:6px;font-family:"Montserrat",sans-serif;font-weight:700;font-size:42px;color:#eef0f4}

/* testimonial */
.t-name{left:194px;top:3355px;font-size:28px;font-weight:600}
.t-role{left:194px;top:3400px;font-size:13px;color:var(--body)}
.t-text{left:194px;top:3470px;width:520px;font-size:13px;line-height:26px;color:var(--body)}
.quote{font-family:"Montserrat",sans-serif;font-weight:700;font-size:60px;color:var(--blue);line-height:1}
.arrow-btn{width:28px;height:28px;border-radius:50%;display:flex;align-items:center;justify-content:center}
.portrait{left:775px;top:3358px;width:232px;height:232px;border-radius:50%;background:linear-gradient(160deg,#e7e9ec,#b8a89a 60%,#8e7e72);border-left:3px solid var(--blue)}
.soc-row{left:832px;top:3604px;display:flex;gap:12px}
.soc-row span{width:28px;height:28px;border-radius:50%;border:1px solid #c5c9d1}
.soc-row span.on{background:var(--blue);border-color:var(--blue)}
.pager{left:572px;top:3662px;display:flex;gap:8px}
.pager i{width:7px;height:7px;border-radius:50%;background:#c9ccd3}
.pager i.on{background:var(--blue)}

/* contact */
.contact-h{left:177px;top:3880px;color:#fff;font-size:26px;font-weight:600}
.contact-p{left:177px;top:3938px;color:#dfe7ff;font-size:12px;line-height:22px;width:360px}
.contact-row{left:177px;display:flex;gap:14px;align-items:center;color:#fff;font-size:14px;line-height:25px;font-weight:500}
.contact-row .ic{width:30px;height:30px;border-radius:50%;background:#fff;display:flex;align-items:center;justify-content:center}
.form-card{left:585px;top:3850px;width:438px;height:455px;background:#fff;border-radius:8px;box-shadow:0 10px 30px rgba(0,0,0,.12);padding:30px 24px}
.form-card h3{font-size:22px;font-weight:600}
.form-card h3 span{color:var(--blue)}
.field{margin-top:14px;height:40px;border:1px solid #cfd2d8;border-radius:6px;font-size:11px;color:var(--muted);padding:12px 16px}
.field.tall{height:118px}
.submit{margin-top:16px;height:44px;width:100%;font-size:13px;border-radius:22px;gap:14px;font-family:"Inter",sans-serif;font-weight:500}

/* footer */
.f-brand{left:0;top:4365px;width:1200px;display:flex;justify-content:center}
.f-brand .brand-name{color:#fff}
.f-text{left:190px;top:4440px;width:820px;text-align:center;color:#cfd0d3;font-size:12px;line-height:24px}
.f-nav{left:0;top:4520px;width:1200px;display:flex;justify-content:center;color:#fff;font-size:12px}
.f-nav span{padding:0 28px;border-right:1px solid #555}
.f-nav span:last-child{border:none}
.f-rule{left:140px;top:4570px;width:920px;height:1px;background:#3d3e41}
.f-contacts{left:0;top:4604px;width:1200px;display:flex;justify-content:center;gap:110px;color:#fff;font-size:12px}
.f-contacts span{display:flex;align-items:center;gap:10px}
.f-rule2{left:0;top:4648px;width:1200px;height:1px;background:#3d3e41}
.f-copy{left:140px;top:4670px;color:#cfd0d3;font-size:11px}
.f-soc{left:936px;top:4666px;display:flex;gap:10px}
.f-soc span{width:20px;height:20px;border-radius:50%;background:#4a4b4f}
.f-soc span.on{background:var(--blue)}
</style>
</head>
<body>

<svg class="bg-layer" viewBox="0 0 1200 4706" aria-hidden="true">
  <path d="M0 1298 Q600 1345 1200 1298 L1200 2008 Q600 2060 0 2030 Z" fill="#f1f2f4"/>
  <path d="M0 2695 Q600 2745 1200 2695 L1200 3270 Q600 3320 0 3290 Z" fill="#f1f2f4"/>
  <path d="M0 3730 Q600 3800 1200 3730 L1200 4290 L0 4290 Z" fill="#2f62f0"/>
  <circle cx="1170" cy="3970" r="80" fill="none" stroke="#4a78f5" stroke-width="26"/>
  <circle cx="20" cy="4060" r="70" fill="none" stroke="#4a78f5" stroke-width="22"/>
  <path d="M0 4280 Q600 4220 1200 4280 L1200 4706 L0 4706 Z" fill="#232426"/>
</svg>

<!-- top bar -->
<div class="abs topbar">
  <div class="socials"><span class="dot-sm"></span><span class="dot-sm"></span><span class="dot-sm"></span><span class="dot-sm"></span></div>
  <div class="item"><span class="ic-circle"><svg width="12" height="10" viewBox="0 0 12 10"><rect x=".5" y=".5" width="11" height="9" fill="none" stroke="#fff"/><path d="M.5 .5 6 5.5 11.5 .5" fill="none" stroke="#fff"/></svg></span>info@valtrobuild.design</div>
  <div class="item"><span class="ic-circle"><svg width="12" height="12" viewBox="0 0 24 24"><path d="M6 2h4l2 5-3 2a12 12 0 0 0 6 6l2-3 5 2v4a2 2 0 0 1-2 2A19 19 0 0 1 4 4a2 2 0 0 1 2-2z" fill="#fff"/></svg></span>+44 (0) 7700 900418</div>
</div>

<!-- header -->
<header class="abs header">
  <div class="brand">
    <span class="brand-mark"></span>
    <div class="brand-name">Valtro Build Design</div>
  </div>
  <nav class="nav">
    <span>HOME</span><span>ABOUT US</span><span>OUR SERVICES</span><span>PORTFOLIO</span>
    <span class="btn">CONTACT US</span>
  </nav>
</header>

<!-- hero -->
<section class="abs hero" role="img" aria-label="Blue background with faint mechanical technical drawing lines"></section>
<h1 class="abs hero-title"><span class="l1">Mechanical</span><br><span class="l2">CAD Design</span></h1>
<div class="abs hero-sub">Cutting Edge Engineering</div>
<div class="abs btn hero-btn">CONTACT US</div>
<div class="abs scroll-btn"><svg width="14" height="14" viewBox="0 0 14 14"><path d="M3 3l4 4 4-4M3 7l4 4 4-4" fill="none" stroke="#333" stroke-width="1.6"/></svg></div>

<!-- about -->
<div class="abs dots" style="left:30px;top:900px;width:90px;height:60px"></div>
<div class="abs dots" style="left:1022px;top:750px;width:80px;height:90px"></div>
<div class="abs photo" style="left:140px;top:825px;width:396px;height:358px;background:linear-gradient(135deg,#c9ccd2,#6f7683 60%,#3b3f48)" role="img" aria-label="Hands sketching on a tablet beside a laptop"></div>
<div class="abs photo" style="left:352px;top:1003px;width:213px;height:213px;background:linear-gradient(160deg,#7d8592,#5a5f68 50%,#c9b29c);border:4px solid #fff" role="img" aria-label="Portrait of the chief engineer"></div>
<h2 class="abs about-title">About Me</h2>
<div class="abs about-div"><b></b><i></i></div>
<p class="abs about-text">Rowan Ellery is the Chief Engineer at Valtro Build Design. He has 11 years experience working as a mechanical design engineer in multiple industries including high performance automotive, consumer products, medical, industrial plus many more. He has worked in multiple roles across a wide range of products.</p>
<div class="abs ticks">
  <span><svg width="18" height="18" viewBox="0 0 18 18"><circle cx="9" cy="9" r="9" fill="#2f62f0"/><path d="M5 9l3 3 5-6" fill="none" stroke="#fff" stroke-width="2"/></svg>15+ Years Experience</span>
  <span><svg width="18" height="18" viewBox="0 0 18 18"><circle cx="9" cy="9" r="9" fill="#2f62f0"/><path d="M5 9l3 3 5-6" fill="none" stroke="#fff" stroke-width="2"/></svg>Manufacturing Focus</span>
</div>
<div class="abs dark-pill">Tell us about your ideas<span class="pill-ic"><svg width="16" height="16" viewBox="0 0 24 24"><path d="M6 2h4l2 5-3 2a12 12 0 0 0 6 6l2-3 5 2v4a2 2 0 0 1-2 2A19 19 0 0 1 4 4a2 2 0 0 1 2-2z" fill="#3a3b3e"/></svg></span></div>

<!-- services -->
<div class="abs sec-head" style="top:1402px"><h2>What We Do You</h2><div class="divider"><i></i><b></b><i></i></div><p>End-to-end mechanical design services engineered for  manufacturability.</p></div>
<article class="abs svc" style="left:141px;top:1535px"><div class="icon"><svg width="30" height="30" viewBox="0 0 24 24"><path d="M12 3l8 4v10l-8 4-8-4V7z M4 7l8 4 8-4 M12 11v10" fill="none" stroke="#fff" stroke-width="1.5"/></svg></div><h3>Bespoke Product Design</h3><p>Innovative design from concept through the full development life cycle</p><div class="pic" role="img" aria-label="Team meeting around a table in a bright office" style="background:linear-gradient(135deg,#d9dde3,#9aa3b0)"></div></article>
<article class="abs svc" style="left:459px;top:1535px"><div class="icon dark"><svg width="28" height="28" viewBox="0 0 24 24"><rect x="4" y="5" width="16" height="12" fill="none" stroke="#fff" stroke-width="1.5"/><path d="M8 20h8" stroke="#fff" stroke-width="1.5"/></svg></div><h3>3D Modelling and Drawings</h3><p>We create 3D CAD, 2D engineering drawings &amp; photorealistic render</p><div class="pic" role="img" aria-label="Tablet showing a 3D model" style="background:linear-gradient(135deg,#6e747d,#3a3e45)"></div></article>
<article class="abs svc" style="left:777px;top:1535px"><div class="icon"><svg width="30" height="30" viewBox="0 0 24 24"><circle cx="12" cy="12" r="4" fill="none" stroke="#fff" stroke-width="1.5"/><circle cx="12" cy="12" r="8" fill="none" stroke="#fff" stroke-width="1.5" stroke-dasharray="3 2"/></svg></div><h3>Design for Manufacture</h3><p>Creating designs optimised for prototype and production manufacture</p><div class="pic" role="img" aria-label="Factory production line with a worker" style="background:linear-gradient(135deg,#a7b7cf,#4a6a98)"></div></article>

<!-- work -->
<div class="abs dots" style="left:1092px;top:2100px;width:90px;height:60px"></div>
<div class="abs sec-head" style="top:2082px"><h2>Our Work &amp; Case Studies</h2><div class="divider"><i></i><b></b><i></i></div><p>A selection of engineering and product design projects demonstrating precision and performance.</p></div>
<article class="abs work" style="left:141px;top:2215px"><div class="pic" role="img" aria-label="Rendered industrial assembly rig" style="background:linear-gradient(180deg,#f2f2f2,#c8c8c8)"></div><h3>Industrial Assembly System</h3><p>Complete redesign of automated assembly line components for manufacturing efficiency improvement.</p><span class="link">View Case Study <svg width="18" height="8" viewBox="0 0 18 8"><path d="M0 4h16M13 1l3 3-3 3" fill="none" stroke="#2f62f0"/></svg></span></article>
<article class="abs work" style="left:459px;top:2215px"><div class="pic" role="img" aria-label="Rendered three-piece alloy wheel" style="background:linear-gradient(180deg,#f4f4f4,#cfcfcf)"></div><h3>3-Piece Alloy Wheels</h3><p>Lightweight suspension component design with FEA validation for high-performance vehicle application.</p><span class="link">View Case Study <svg width="18" height="8" viewBox="0 0 18 8"><path d="M0 4h16M13 1l3 3-3 3" fill="none" stroke="#2f62f0"/></svg></span></article>
<article class="abs work" style="left:777px;top:2215px"><div class="pic" role="img" aria-label="Rendered medical device enclosure on a mount" style="background:linear-gradient(180deg,#efefef,#bdbdbd)"></div><h3>Medical Device Enclosure</h3><p>Ergonomic and manufacturable enclosure design for a portable medical diagnostic device.</p><span class="link">View Case Study <svg width="18" height="8" viewBox="0 0 18 8"><path d="M0 4h16M13 1l3 3-3 3" fill="none" stroke="#2f62f0"/></svg></span></article>
<div class="abs btn cta-blue">View All Case Study<span class="pill-ic"><svg width="16" height="16" viewBox="0 0 24 24"><path d="M6 2h4l2 5-3 2a12 12 0 0 0 6 6l2-3 5 2v4a2 2 0 0 1-2 2A19 19 0 0 1 4 4a2 2 0 0 1 2-2z" fill="#2f62f0"/></svg></span></div>

<!-- process -->
<div class="abs dots" style="left:30px;top:2830px;width:90px;height:60px"></div>
<div class="abs sec-head" style="top:2808px"><h2>How We Work</h2><div class="divider"><i></i><b></b><i></i></div><p>A selection of engineering and product design projects demonstrating precision and performance.</p></div>
<article class="abs step" style="left:134px;top:2943px"><div class="hd"><span class="ic"><svg width="22" height="22" viewBox="0 0 24 24"><circle cx="12" cy="12" r="8" fill="none" stroke="#fff" stroke-width="1.5"/><circle cx="8.5" cy="12" r="1" fill="#fff"/><circle cx="12" cy="12" r="1" fill="#fff"/><circle cx="15.5" cy="12" r="1" fill="#fff"/></svg></span>Consultation</div><p>We begin with comprehensive consultation to understand your technical requirements, constraints, &amp; objectives.</p><span class="link">Find out more <svg width="18" height="8" viewBox="0 0 18 8"><path d="M0 4h16M13 1l3 3-3 3" fill="none" stroke="#2f62f0"/></svg></span><span class="num">01</span></article>
<article class="abs step" style="left:375px;top:2943px"><div class="hd"><span class="ic"><svg width="22" height="22" viewBox="0 0 24 24"><rect x="4" y="5" width="16" height="12" fill="none" stroke="#fff" stroke-width="1.5"/><path d="M8 20h8" stroke="#fff" stroke-width="1.5"/></svg></span>Design</div><p>Development of initial concepts, 3D models, and functional prototypes for evaluation and refinement.</p><span class="link">Find out more <svg width="18" height="8" viewBox="0 0 18 8"><path d="M0 4h16M13 1l3 3-3 3" fill="none" stroke="#2f62f0"/></svg></span><span class="num">02</span></article>
<article class="abs step" style="left:615px;top:2943px"><div class="hd"><span class="ic"><svg width="22" height="22" viewBox="0 0 24 24"><circle cx="12" cy="12" r="8" fill="none" stroke="#fff" stroke-width="1.5"/><path d="M8 12l3 3 5-6" fill="none" stroke="#fff" stroke-width="1.5"/></svg></span>Validation</div><p>Rigorous testing and analysis including FEA, CFD, and tolerance analysis to validate design performance.</p><span class="link">Find out more <svg width="18" height="8" viewBox="0 0 18 8"><path d="M0 4h16M13 1l3 3-3 3" fill="none" stroke="#2f62f0"/></svg></span><span class="num">03</span></article>
<article class="abs step" style="left:855px;top:2943px"><div class="hd"><span class="ic"><svg width="22" height="22" viewBox="0 0 24 24"><path d="M12 3l8 4v10l-8 4-8-4V7z M4 7l8 4 8-4 M12 11v10" fill="none" stroke="#fff" stroke-width="1.5"/></svg></span>Delivery</div><p>Creation of comprehensive engineering drawings, Bill of Materials, and manufacturing documentation.</p><span class="link">Find out more <svg width="18" height="8" viewBox="0 0 18 8"><path d="M0 4h16M13 1l3 3-3 3" fill="none" stroke="#2f62f0"/></svg></span><span class="num">04</span></article>

<!-- testimonial -->
<div class="abs t-name heading">Martin J Halloway</div>
<div class="abs t-role">Project Manager AT Brightline Systems</div>
<div class="abs quote" style="left:192px;top:3428px">“</div>
<p class="abs t-text">"Rowan went above and beyond in all aspects of the job. He identified issues with the design that I had not foreseen, rebuilt the design from scratch to ensure no aspect was overlooked, and provided solutions immediately to challenges he found. After some explaining about the end use of the product, he was able to offer ways to optimise the product further than I had thought.</p>
<div class="abs quote" style="left:694px;top:3580px">”</div>
<div class="abs arrow-btn" style="left:123px;top:3499px;background:#d7d9de"><svg width="8" height="10" viewBox="0 0 8 10"><path d="M6 1 2 5l4 4" fill="none" stroke="#fff" stroke-width="1.6"/></svg></div>
<div class="abs arrow-btn" style="left:1048px;top:3499px;background:var(--blue)"><svg width="8" height="10" viewBox="0 0 8 10"><path d="M2 1l4 4-4 4" fill="none" stroke="#fff" stroke-width="1.6"/></svg></div>
<div class="abs portrait" role="img" aria-label="Portrait photo of the client"></div>
<div class="abs soc-row"><span></span><span class="on"></span><span></span></div>
<div class="abs dots" style="left:240px;top:3630px;width:94px;height:60px"></div>
<div class="abs pager"><i></i><i class="on"></i><i></i><i></i></div>

<!-- contact -->
<h2 class="abs contact-h">Start Your Journey With Us</h2>
<p class="abs contact-p">Let's discuss your requirements and find the right solution.<br>Trusted by engineers, founders, and manufacturers.</p>
<div class="abs contact-row" style="top:4018px"><span class="ic"><svg width="14" height="14" viewBox="0 0 24 24"><path d="M6 2h4l2 5-3 2a12 12 0 0 0 6 6l2-3 5 2v4a2 2 0 0 1-2 2A19 19 0 0 1 4 4a2 2 0 0 1 2-2z" fill="#2f62f0"/></svg></span><div>Call Now<br>+44 (0) 7700 900418</div></div>
<div class="abs contact-row" style="top:4090px"><span class="ic"><svg width="14" height="12" viewBox="0 0 12 10"><rect x=".5" y=".5" width="11" height="9" fill="none" stroke="#2f62f0"/><path d="M.5 .5 6 5.5 11.5 .5" fill="none" stroke="#2f62f0"/></svg></span><div>Email Now<br>info@valtrobuild.design</div></div>
<form class="abs form-card">
  <h3>Field The Below <span>Details</span></h3>
  <div class="field" style="margin-top:18px">First Name</div>
  <div class="field">Last Name</div>
  <div class="field">Email ID</div>
  <div class="field tall">Message</div>
  <div class="btn submit">Submit Your Details <svg width="18" height="8" viewBox="0 0 18 8"><path d="M0 4h16M13 1l3 3-3 3" fill="none" stroke="#fff"/></svg></div>
</form>

<!-- footer -->
<div class="abs f-brand"><div class="brand"><span class="brand-mark"></span><div class="brand-name">Valtro Build Design</div></div></div>
<p class="abs f-text">Welcome to Valtro Build Design. We are a UK based design consultancy offering a comprehensive mechanical and product design service from initial concepts through to full volume production.</p>
<div class="abs f-nav"><span>Home</span><span>About Us</span><span>Services</span><span>Our Work</span><span>Our Process</span></div>
<div class="abs f-rule"></div>
<div class="abs f-contacts">
  <span><svg width="12" height="14" viewBox="0 0 12 14"><path d="M6 13S1 8 1 5a5 5 0 0 1 10 0c0 3-5 8-5 8z" fill="#fff"/><circle cx="6" cy="5" r="1.8" fill="#232426"/></svg>We're based in North Yorkshire, UK.</span>
  <span><svg width="13" height="10" viewBox="0 0 12 10"><rect x=".5" y=".5" width="11" height="9" fill="#fff"/><path d="M.5 .5 6 5.5 11.5 .5" fill="none" stroke="#232426"/></svg>info@valtrobuild.design</span>
  <span><svg width="12" height="12" viewBox="0 0 24 24"><path d="M6 2h4l2 5-3 2a12 12 0 0 0 6 6l2-3 5 2v4a2 2 0 0 1-2 2A19 19 0 0 1 4 4a2 2 0 0 1 2-2z" fill="#fff"/></svg>+44 (0) 7700 900418</span>
</div>
<div class="abs f-rule2"></div>
<div class="abs f-copy">© 2025 Valtro Build Design</div>
<div class="abs f-soc"><span></span><span></span><span class="on"></span><span></span></div>

</body>
</html>
```